Wholesale in Gold Jewellery & Gold Bullion

We are an established gold jewellery and gold bullion wholesaler selling these products to international clients. We already have a name and logo of our company, hence please view attached current card design. We need a completely new design to compliment our business and industry and the final design should be new and elegant.

Contact Information for Business Card

New card details must be same as per current card. Like logo, name, tel no. & etc.

Colors

Designer to choose colors to be used in the design.

```html
<!DOCTYPE html>
<html lang="en">
<head>
<meta charset="utf-8">
<title>Ravel &amp; Co — Business Card</title>
<link rel="stylesheet" href="https://fonts.googleapis.com/css2?family=Bebas+Neue&family=Open+Sans:wght@400&display=swap">
<style>
  :root {
    --backdrop: #2b2b2b;
    --card: #121212;
    --gold: #e89f12;
    --text-light: #c9c9c9;
    --text-muted: #9a9a9a;
    --divider: #6a6a6a;
  }
  * { box-sizing: border-box; margin: 0; padding: 0; }
  html, body { width: 1200px; height: 900px; overflow: hidden; }
  body {
    background: var(--backdrop);
    font-family: "Open Sans", Arial, sans-serif;
    position: relative;
  }
  .card {
    position: absolute;
    left: 320px;
    width: 560px;
    height: 320px;
    background: var(--card);
    overflow: hidden;
  }
  .card::after {
    content: "";
    position: absolute;
    left: 0; right: 0; bottom: 0;
    height: 9px;
    background: var(--gold);
  }
  .card-front { top: 110px; }
  .card-back { top: 470px; }

  .brand {
    position: absolute;
    left: 0; right: 0; top: 124px;
    text-align: center;
  }
  .brand-name {
    font-family: "Bebas Neue", Impact, sans-serif;
    font-size: 52px;
    letter-spacing: 1px;
    color: var(--gold);
    line-height: 1;
  }

  .identity {
    position: absolute;
    right: 290px;
    top: 128px;
    text-align: right;
  }
  .person-name {
    font-family: "Bebas Neue", Impact, sans-serif;
    font-size: 27px;
    color: var(--gold);
    letter-spacing: 0.5px;
    line-height: 1;
  }
  .person-role {
    font-size: 14px;
    color: var(--text-muted);
    margin-top: 2px;
  }
  .divider {
    position: absolute;
    left: 284px;
    top: 120px;
    width: 1px;
    height: 92px;
    background: var(--divider);
  }
  .contacts {
    position: absolute;
    left: 300px;
    top: 118px;
    list-style: none;
  }
  .contacts li {
    display: flex;
    align-items: center;
    gap: 9px;
    font-size: 14px;
    color: var(--text-light);
    line-height: 22px;
  }
  .contacts svg { width: 12px; height: 12px; fill: var(--gold); flex: none; }
  .address {
    position: absolute;
    left: 118px;
    top: 248px;
    font-size: 14px;
    color: var(--text-light);
  }
</style>
</head>
<body>
  <section class="card card-front" aria-label="Card front">
    <div class="brand">
      <span class="brand-name">Ravel &amp; Co</span>
    </div>
  </section>

  <section class="card card-back" aria-label="Card back">
    <div class="identity">
      <p class="person-name">Arjun Teymar</p>
      <p class="person-role">Director</p>
    </div>
    <span class="divider"></span>
    <ul class="contacts">
      <li>
        <svg viewBox="0 0 12 12" aria-hidden="true"><path d="M1 4c0-2 2-3 5-3s5 1 5 3v1H8.5V3.8h-5V5H1zM3 6h6l2 5H1z"/></svg>
        +65 6100 2480
      </li>
      <li>
        <svg viewBox="0 0 12 12" aria-hidden="true"><path d="M3 0h6a1 1 0 0 1 1 1v10a1 1 0 0 1-1 1H3a1 1 0 0 1-1-1V1a1 1 0 0 1 1-1zm0.5 1.5v7.5h5V1.5zM6 10a.6.6 0 1 0 0 1.2A.6.6 0 0 0 6 10z"/></svg>
        +65 9100 3571
      </li>
      <li>
        <svg viewBox="0 0 12 12" aria-hidden="true"><path d="M3 0h6v3H3zM1 4h10a1 1 0 0 1 1 1v4H10v3H2V9H0V5a1 1 0 0 1 1-1zm2.5 4.5v2h5v-2z"/></svg>
        +65 6100 2481
      </li>
      <li>
        <svg viewBox="0 0 12 12" aria-hidden="true"><path d="M0 2h12v8H0zm1.2 1.2L6 6.6l4.8-3.4z"/></svg>
        arjun@ravelco.com
      </li>
    </ul>
    <p class="address">12 Lorong Kemuning, Singapore 208815</p>
  </section>
</body>
</html>
```